Design a Flooring flyer based on out information

We are a flooring company who specialise in supply & installation of high quality flooring (Laminate, SPC vinyl planks and engineered timber)

The colours in flyer should only consist the same colours in business logo as attached

Flyer needs to show customers we offer samples for free delivered to see quality and colours. This can only be ordered via our website.

Contact number: 1300 482 915

www.brantleyfloorcraft.com.au

instagram: brantleycraftcollective

Inregards to texts for flyer.. I will attach our body content of 'about us' Please add some key points in flyer

About Us

Marcus Brantley founded Brantley’s Floorcraft Group with one goal in mind – quality flooring equipment. Our team is made up of flooring professionals who have had extensive experience with flooring installation themselves. Therefore, we are experts at equipping customers with the right products they need to succeed.

The team at Brantley’s Floorcraft Group have had mastered all sorts of flooring technology as we are always focused on innovation and advancement. For example, our expert team has mastered the correct click system that floors need to be suitable for water spills, surface scratches, and foot traffic impact. This is just one of the ways our hands-on team strives to provide our customers with the innovative flooring technology.

Additionally, we make sure that our products are specifically suited to flourish in the Australian environment, and all of our equipment have been approved by Australian standards. Rain, drought or shine, our products are built to survive in Australian weather.

At Brantley’s Floorcraft Group, we work with you to ensure the best outcome for your unique situation. Just contact our friendly and knowledgeable team today to find out more.

Target Market(s)

Home owners

Requirements
Must have
• Logo colours, modern and expensive

```html
<!DOCTYPE html>
<html lang="en">
<head>
<meta charset="utf-8">
<title>Brantley's Floorcraft Group – Flyer</title>
<link href="https://fonts.googleapis.com/css2?family=Montserrat:wght@400;500;600;700&display=swap" rel="stylesheet">
<style>
  :root{
    --green:#7dc142;
    --green-dark:#5fa42c;
    --charcoal:#4a4a4c;
    --charcoal-deep:#3d3d3f;
    --ink:#444446;
    --white:#ffffff;
    --floor-grey:#8a8886;
    --room-light:#e9e6e1;
  }
  *{margin:0;padding:0;box-sizing:border-box}
  html,body{width:951px;height:1200px;overflow:hidden;background:var(--charcoal)}
  .flyer{position:relative;width:951px;height:1200px;overflow:hidden;font-family:"Montserrat",sans-serif;color:var(--ink)}
  .backdrop{position:absolute;inset:0;width:951px;height:1200px}
  .photo{position:absolute;inset:0}
  .photo--living{
    background:linear-gradient(180deg,var(--room-light) 0%,#d8d5d0 38%,#9b9894 60%,#6f6d6b 100%);
    clip-path:path("M0,0 H540 C566,150 586,300 592,462 C400,474 200,486 0,500 Z");
  }
  .photo--kitchen{
    background:linear-gradient(180deg,#f1efeb 0%,#dcd8d2 35%,#a9a49e 60%,var(--floor-grey) 100%);
    clip-path:path("M624,488 C740,478 850,470 951,464 V1200 H566 C606,1000 628,760 624,488 Z");
  }

  .brand{position:absolute;left:625px;top:128px;width:315px;text-align:center}
  .brand__mark{width:40px;height:40px;margin:0 auto 22px;background:var(--green)}
  .brand__name{font-weight:600;color:var(--charcoal);font-size:34px;line-height:1.05;letter-spacing:1px}
  .brand__name span{display:block;font-size:12px;letter-spacing:6px;margin-top:6px;color:var(--green)}
  .brand__services{margin-top:7px;font-size:6.5px;font-weight:700;letter-spacing:1.6px;color:var(--charcoal-deep)}

  .samples{position:absolute;left:640px;top:318px;width:290px;text-align:center}
  .samples__title{font-size:15px;font-weight:700;color:var(--green-dark);letter-spacing:.5px}
  .samples__note{margin-top:3px;font-size:9px;font-weight:600;color:var(--charcoal)}
  .key-points{margin-top:10px;list-style:none;display:flex;flex-direction:column;gap:4px;font-size:9.5px;font-weight:600;color:var(--charcoal)}
  .key-points li::before{content:"";display:inline-block;width:6px;height:6px;margin-right:6px;background:var(--green);vertical-align:1px}

  .about-tag{position:absolute;left:0;top:555px;width:224px;height:46px;background:linear-gradient(90deg,var(--green-dark),var(--green));border-radius:0 23px 23px 0;box-shadow:4px 6px 10px rgba(0,0,0,.25);color:var(--white);font-weight:600;font-size:29px;line-height:46px;padding-left:26px}

  .about-copy{position:absolute;left:37px;top:632px;width:474px;font-size:10.6px;font-weight:500;line-height:14.5px;text-align:justify;color:var(--ink)}
  .about-copy p{margin-bottom:30px}

  .callout{position:absolute;left:37px;width:474px;text-align:center;font-weight:700;font-size:13.5px;line-height:17px;text-transform:uppercase;color:var(--charcoal)}
  .callout--work{top:929px}
  .callout--contact{top:1008px;color:var(--green-dark)}
  .accent{color:var(--green-dark)}

  .contact{position:absolute;top:1098px;display:flex;align-items:center;gap:6px;color:var(--white);font-weight:700}
  .contact--phone{left:37px;font-size:19px}
  .contact--social{left:260px;font-size:13.5px;text-transform:uppercase}
  .contact__dot{width:24px;height:24px;border:2.5px solid var(--white);border-radius:50%}
  .website{position:absolute;left:120px;top:1148px;width:296px;height:31px;border-radius:6px;background:var(--green);box-shadow:0 6px 10px rgba(0,0,0,.35);color:var(--white);font-weight:700;font-size:13px;line-height:31px;text-align:center}
</style>
</head>
<body>
<main class="flyer">
  <svg class="backdrop" viewBox="0 0 951 1200" aria-hidden="true">
    <defs>
      <linearGradient id="panel-fade" x1="0" y1="0" x2="1" y2="1">
        <stop offset="0" stop-color="#ffffff"/>
        <stop offset="1" stop-color="#dcdcdd"/>
      </linearGradient>
    </defs>
    <rect width="951" height="1200" fill="#4a4a4c"/>
    <path d="M548,0 H951 V448 C840,454 720,462 612,470 C604,300 584,140 548,0 Z" fill="#ffffff"/>
    <path d="M612,470 C720,460 840,452 951,446 V466 C840,472 730,480 614,490 Z" fill="#7dc142"/>
    <path d="M0,494 C200,482 400,470 598,458 L600,476 C400,498 200,518 0,536 Z" fill="#7dc142"/>
    <path d="M0,550 C200,532 400,522 576,520 C574,720 560,900 528,1075 H0 Z" fill="url(#panel-fade)"/>
    <path d="M532,0 H552 C598,200 626,460 622,640 C618,860 596,1040 556,1200 H532 C572,1040 594,860 598,640 C600,440 574,200 532,0 Z" fill="#7dc142"/>
  </svg>

  <div class="photo photo--living" role="img" aria-label="Bright living room with a white sofa, coffee table and grey wide-plank laminate flooring"></div>
  <div class="photo photo--kitchen" role="img" aria-label="Open kitchen with bar stools and light grey timber-look vinyl plank flooring"></div>

  <header class="brand">
    <div class="brand__mark"></div>
    <div class="brand__name">BRANTLEY'S<span>CRAFT COLLECTIVE</span></div>
    <div class="brand__services">CARPENTRY | FLOORING | FLOOR LEVELLING</div>
  </header>

  <section class="samples">
    <p class="samples__title">FREE SAMPLES DELIVERED</p>
    <p class="samples__note">See the quality &amp; colours at home – order only at www.brantleyfloorcraft.com.au</p>
    <ul class="key-points">
      <li>Supply &amp; installation of high quality flooring</li>
      <li>Laminate · SPC vinyl planks · Engineered timber</li>
      <li>Approved by Australian standards</li>
    </ul>
  </section>

  <h2 class="about-tag">ABOUT US</h2>

  <section class="about-copy">
    <p>Marcus Brantley founded Brantley’s Floorcraft Group with one goal in mind – quality flooring equipment. Our team is made up of flooring professionals who have had extensive experience with flooring installation themselves. Therefore, we are experts at equipping customers with the right products they need to succeed.</p>
    <p>The team at Brantley’s Floorcraft Group have had mastered all sorts of flooring technology as we are always focused on innovation and advancement. For example, our expert team has mastered the correct click system that floors need to be suitable for water spills, surface scratches, and foot traffic impact. This is just one of the ways our hands-on team strives to provide our customers with the innovative flooring technology.</p>
    <p>Additionally, we make sure that our products are specifically suited to flourish in the Australian environment, and all of our equipment have been approved by Australian standards. Rain, drought or shine, our products are built to survive in Australian weather.</p>
  </section>

  <p class="callout callout--work"><span class="accent">At Brantley’s Floorcraft Group</span>, we work with you<br>to ensure the best outcome for<br>your unique situation.</p>
  <p class="callout callout--contact">Just contact our friendly and knowledgeable<br>team today to find out more.</p>

  <div class="contact contact--phone">
    <svg width="24" height="24" viewBox="0 0 24 24" aria-hidden="true"><circle cx="12" cy="12" r="10.5" fill="none" stroke="#fff" stroke-width="2"/><path d="M8.2,6.5 l2,2.4 -1.1,1.4 c.8,1.7 2,2.9 3.7,3.7 l1.4-1.1 2.4,2 -1.3,1.9 c-4.2-.4 -8.2-4.4 -8.6-8.6 Z" fill="#fff"/></svg>
    1300 482 915
  </div>
  <div class="contact contact--social"><span class="contact__dot"></span>brantleycraftcollective</div>
  <div class="website">www.brantleyfloorcraft.com.au</div>
</main>
</body>
</html>
```